Business Card Design Project

we are a new company , see www.chatharborlane.com
we also have a concurrent flyer deign competition so you may also wish to enter that.
We provide live customer support services for websites.
We cater for mainly european market.
info for card:
Martin Colbrook
Director
p: +353 (0)90 612 8051
f: +353 (0)90 612 8062
m: +353 (0)86 507 4926
e: martin@chatharborlane.com
w: www.chatharborlane.com
The card does not have to use the exact colour on the website but should ahve something of the general feel of it. It should have modern corporate feel without brash coulours. we will upload the logo and card should be standard european size 85x55mm
Target Market(s)
Online business owners
Industry/Entity Type
Business
Look and feel
Each slider illustrates characteristics of the customer's brand and the style your logo design should communicate.

```html
<!DOCTYPE html>
<html lang="en">
<head>
<meta charset="utf-8">
<title>Chat Harbor Lane – Business Card</title>
<link href="https://fonts.googleapis.com/css2?family=Open+Sans:wght@400;600;700;800&display=swap" rel="stylesheet">
<style>
  :root {
    --stage: #a1a1a1;
    --paper: #ffffff;
    --brand-blue: #318bc4;
    --name-blue: #2d7bb6;
    --ink: #4a4a4a;
    --slate: #56514f;
  }
  * { margin: 0; padding: 0; box-sizing: border-box; }
  html, body { width: 1200px; height: 900px; overflow: hidden; }
  body {
    background: var(--stage);
    font-family: "Open Sans", Arial, sans-serif;
    position: relative;
  }
  .card {
    position: absolute;
    left: 317px;
    width: 579px;
    height: 375px;
    background: var(--paper);
    overflow: hidden;
  }
  .card--front { top: 36px; }
  .card--back { top: 493px; }

  .side-band {
    position: absolute;
    left: 9px; top: 9px;
    width: 40px; height: 356px;
    background: var(--brand-blue);
  }
  .wordmark {
    position: absolute;
    display: flex;
    align-items: center;
    gap: 10px;
    color: var(--slate);
    font-weight: 800;
    text-transform: uppercase;
    white-space: nowrap;
  }
  .wordmark__square { background: var(--brand-blue); flex: none; }
  .card--front .wordmark {
    right: 18px; top: 22px;
    font-size: 24px; letter-spacing: 0.3px;
  }
  .card--front .wordmark__square { width: 17px; height: 17px; }

  .identity {
    position: absolute;
    left: 0; right: 0; top: 140px;
    text-align: center;
    padding-left: 20px;
  }
  .identity__name {
    color: var(--name-blue);
    font-weight: 700;
    font-size: 37px;
    line-height: 1.1;
    letter-spacing: -0.5px;
  }
  .identity__role {
    color: var(--ink);
    font-size: 29px;
    line-height: 1.15;
  }

  .contacts {
    position: absolute;
    left: 328px; right: 10px; top: 283px;
    font-size: 16.5px;
    color: var(--ink);
    line-height: 21px;
    white-space: nowrap;
  }
  .contacts__row { display: flex; }
  .contacts__label {
    width: 62px;
    color: var(--name-blue);
    font-weight: 700;
    font-size: 12px;
    text-transform: uppercase;
    align-self: center;
  }
  .contacts__email {
    color: var(--name-blue);
    font-weight: 600;
    font-size: 13.5px;
    text-transform: uppercase;
    margin-top: 2px;
  }

  .back-panel {
    position: absolute;
    left: 5px; top: 6px;
    width: 559px; height: 320px;
    background: var(--brand-blue);
  }
  .card--back .wordmark {
    left: 0; right: 0; top: 0; bottom: 0;
    justify-content: center;
    font-size: 40px;
    letter-spacing: 0;
    gap: 14px;
  }
  .card--back .wordmark__square { width: 30px; height: 30px; background: var(--slate); }
</style>
</head>
<body>
  <section class="card card--front">
    <div class="side-band"></div>
    <div class="wordmark"><span class="wordmark__square"></span>Chat Harbor Lane</div>
    <div class="identity">
      <h1 class="identity__name">Martin Colbrook</h1>
      <p class="identity__role">Director</p>
    </div>
    <div class="contacts">
      <div class="contacts__row"><span class="contacts__label">Fax:</span><span>+353 (0)90 612 8062</span></div>
      <div class="contacts__row"><span class="contacts__label">Phone:</span><span>+353 (0)90 612 8051</span></div>
      <div class="contacts__row"><span class="contacts__label">Mobile:</span><span>+353 (0)86 507 4926</span></div>
      <div class="contacts__email">martin@chatharborlane.com</div>
    </div>
  </section>

  <section class="card card--back">
    <div class="back-panel">
      <div class="wordmark"><span class="wordmark__square"></span>Chat Harbor Lane</div>
    </div>
  </section>
</body>
</html>
```